New Business Card Design Project

I would like my card design to look exactly like the logo, design, layout, and print of the current attached file. The only change I would like made would be for the print to say THE KMW GROUP instead of THE HALLORAN GROUP. Basically, just replace his group name with my group name. I would also like the backgroud to be the same texture and color as the attached file. I love the dark blue lettering and house logo on the card.

I am completely open to the rest of the card design. I just want something clean and simple. Only basic contact info required on the card. Maybe just name: Kyle M Warrick and cell # 555.914.2087 and email kyle@orchidhomesagent.com

```html
<!DOCTYPE html>
<html lang="en">
<head>
<meta charset="utf-8">
<title>The KMW Group – Business Card</title>
<link href="https://fonts.googleapis.com/css2?family=Arimo:wght@700&display=swap" rel="stylesheet">
<style>
  :root {
    --page-bg: #e4e5ea;
    --card-stock: #dcdbd6;
    --card-edge: #cfcec8;
    --ink-navy: #14163a;
  }
  * { margin: 0; padding: 0; box-sizing: border-box; }
  html, body {
    width: 1000px;
    height: 1200px;
    overflow: hidden;
  }
  body {
    position: relative;
    background: var(--page-bg);
    font-family: "Arimo", Arial, sans-serif;
    font-weight: 700;
    color: var(--ink-navy);
  }
  .card {
    position: absolute;
    left: 120px;
    width: 760px;
    height: 434px;
    background: var(--card-stock);
    border: 1px solid var(--card-edge);
  }
  .card--front { top: 165px; }
  .card--back  { top: 685px; }

  .brand {
    position: absolute;
    display: flex;
    align-items: center;
  }
  .brand__square {
    background: var(--ink-navy);
    flex: none;
  }
  .brand__name {
    text-transform: uppercase;
    line-height: 1.18;
  }

  .card--front .brand { left: 198px; top: 142px; }
  .card--front .brand__square { width: 120px; height: 120px; margin-right: 30px; }
  .card--front .brand__name { font-size: 32px; }

  .card--back .brand { left: 52px; top: 45px; }
  .card--back .brand__square { width: 48px; height: 48px; margin-right: 14px; }
  .card--back .brand__name { font-size: 13px; }

  .contact-list {
    position: absolute;
    left: 282px;
    top: 222px;
    list-style: none;
  }
  .contact-list__item {
    display: flex;
    align-items: center;
    height: 68px;
    font-size: 26px;
  }
  .contact-list__icon {
    width: 44px;
    height: 38px;
    margin-right: 26px;
    flex: none;
    fill: var(--ink-navy);
  }
</style>
</head>
<body>

  <section class="card card--front">
    <div class="brand">
      <span class="brand__square"></span>
      <p class="brand__name">The<br>KMW<br>Group</p>
    </div>
  </section>

  <section class="card card--back">
    <div class="brand">
      <span class="brand__square"></span>
      <p class="brand__name">The<br>KMW<br>Group</p>
    </div>

    <ul class="contact-list">
      <li class="contact-list__item">
        <svg class="contact-list__icon" viewBox="0 0 44 38" aria-hidden="true">
          <circle cx="22" cy="11" r="9"/>
          <path d="M4 38 V31 Q4 22 15 21 H29 Q40 22 40 31 V38 Z"/>
        </svg>
        <span class="contact-list__text">Kyle M Warrick</span>
      </li>
      <li class="contact-list__item">
        <svg class="contact-list__icon" viewBox="0 0 44 38" aria-hidden="true">
          <path d="M8 3 L15 1 L20 11 L15 15 Q19 24 27 28 L31 23 L41 28 L39 35 Q36 38 30 37 Q15 33 7 18 Q4 10 8 3 Z"/>
        </svg>
        <span class="contact-list__text">555.914.2087</span>
      </li>
      <li class="contact-list__item">
        <svg class="contact-list__icon" viewBox="0 0 44 38" aria-hidden="true">
          <rect x="3" y="6" width="38" height="27" fill="none" stroke="var(--ink-navy)" stroke-width="2.5"/>
          <path d="M3 6 L22 22 L41 6 M3 33 L17 18 M41 33 L27 18" fill="none" stroke="var(--ink-navy)" stroke-width="2.5"/>
        </svg>
        <span class="contact-list__text">kyle@orchidhomesagent.com</span>
      </li>
    </ul>
  </section>

</body>
</html>
```